Children's book series redesign

Redesign required of existing children's book series.
I have two different styles of books requiring a redesign.
For both styles of book, this will include:
- a cover page
- title page
- back of book
- internal page of 'Teaching Notes'
All high resolution images and text will be provided.
Final output includes design template in an Adobe Creative Cloud programme (e.g., In Design), plus finished copies of all texts using the agreed template.
Book designs can be related but need to look visually distinct and be clearly branded with Bright Path Reading Method and University of Wexmoor logo (provided).
Total numbers of texts:
21 x small readers (see attached example)
14 x larger readers (see attached example)
To bid for this job, please submit a concept design plan for both types of books (including cover, back page and 'teaching notes' page.
Target Market(s)
3-5 year old children, teachers and parents

```html
<!DOCTYPE html>
<html lang="en">
<head>
<meta charset="utf-8">
<title>Teaching Notes – Reading Practice Spread</title>
<link href="https://fonts.googleapis.com/css2?family=Lexend:wght@300;400;500;600&display=swap" rel="stylesheet">
<style>
  :root {
    --backdrop: #d2d2d4;
    --paper: #f4f4f3;
    --ink: #1f1d1b;
    --accent-dot: #e0a062;
    --cover-light: #f0cd9e;
    --cover-mid: #e6b27a;
    --cover-dark: #b9722f;
    --tile-light: #ecc9ac;
    --tile-mid: #dcae8e;
    --tile-dark: #c99678;
    --tile-ink: #2a1d14;
  }
  * { box-sizing: border-box; margin: 0; padding: 0; }
  html, body {
    width: 1200px; height: 900px; overflow: hidden;
    background: var(--backdrop);
    font-family: "Lexend", sans-serif;
    color: var(--ink);
  }
  .spread {
    position: absolute; left: 100px; top: 200px;
    width: 1000px; height: 500px;
    display: flex;
    box-shadow: 0 20px 40px rgba(60,60,70,.18);
  }
  .page { width: 500px; height: 500px; position: relative; }
  .page--notes-cover {
    background: linear-gradient(100deg, var(--cover-mid) 0%, var(--cover-light) 45%, var(--cover-mid) 80%, var(--cover-dark) 100%);
    display: flex; align-items: center; justify-content: center;
  }
  .notes-title {
    color: #fff; font-weight: 500; font-size: 17px; letter-spacing: 3px;
  }
  .page--practice {
    background: var(--paper);
    padding: 56px 50px 0 48px;
  }
  .page-frame {
    position: absolute; inset: 12px 12px 12px 6px;
    border: 1px dotted var(--accent-dot);
    pointer-events: none;
  }
  .practice-heading {
    font-size: 10.5px; font-weight: 600; letter-spacing: 1.6px;
  }
  .practice-intro, .practice-guide {
    font-size: 8.6px; font-weight: 300; line-height: 1.5;
    max-width: 340px;
  }
  .practice-intro { margin-top: 58px; }
  .section-label {
    font-size: 7px; font-weight: 600; letter-spacing: 1px;
    margin-top: 22px; margin-bottom: 6px;
  }
  .practice-guide { margin-top: 34px; }
  .tile-row { display: flex; gap: 4px; }
  .tile {
    height: 20px; min-width: 20px; padding: 0 6px;
    border-radius: 3px;
    display: flex; align-items: center; justify-content: center;
    font-size: 10.5px; font-weight: 500; color: var(--tile-ink);
    background: var(--tile-mid);
  }
  .tile:nth-child(3n+1) { background: var(--tile-light); }
  .tile:nth-child(3n) { background: var(--tile-dark); }
</style>
</head>
<body>
  <main class="spread">
    <section class="page page--notes-cover">
      <h1 class="notes-title">TEACHING NOTES</h1>
    </section>

    <section class="page page--practice">
      <div class="page-frame"></div>
      <h2 class="practice-heading">READING PRACTICE</h2>
      <p class="practice-intro">This story provides children with practice in decoding and understanding short words using carefully selected focus sounds.</p>

      <h3 class="section-label">FOCUS SOUNDS</h3>
      <div class="tile-row">
        <span class="tile">m</span><span class="tile">d</span><span class="tile">p</span><span class="tile">t</span><span class="tile">n</span><span class="tile">a</span><span class="tile">e</span><span class="tile">o</span>
      </div>

      <p class="practice-guide">Introduce the text and read the story aloud together, pointing to each word as you read. Help children sound out some of the regular words and then blend the sounds together. When reading other new words simply tell children the words as you read together. Give plenty of praise for children’s reading attempts and encourage re-reading to build accuracy and fluency.</p>

      <h3 class="section-label">REGULAR WORDS FOR SOUNDING OUT</h3>
      <div class="tile-row">
        <span class="tile">tap</span><span class="tile">mat</span><span class="tile">pat</span><span class="tile">Tad</span><span class="tile">Dad</span><span class="tile">pot</span><span class="tile">pet</span><span class="tile">mad</span>
      </div>

      <h3 class="section-label">OTHER WORDS TO TELL YOUR CHILD</h3>
      <div class="tile-row">
        <span class="tile">Mia</span><span class="tile">a</span><span class="tile">no</span><span class="tile">her</span><span class="tile">Mum</span><span class="tile">is</span>
      </div>
    </section>
  </main>
</body>
</html>
```